依頼詳細
宮城県仙台市に新たにオープンするサロンのチラシの依頼になります。
ビルの1Fには高級時計店、隣のビルは老舗高級百貨店があります。
都会的な洗練されたデザインにしてほしいです。
記載項目

K.A.Z by sorvique
022-614-5027
仙台アーケード街に2022.6.1 NEW OPEN
サイズ
A5
ページ数
両面
希望イメージ
シンプル 複雑
単色 カラフル
暗い 明るい
日常 高級
遊び心 厳粛
未来的 伝統的
女性的 男性的
希望する色
グレー系
納品ファイル
• 高解像度JPG (.jpg)
• フォトショップ形式 (.psd)
補足説明
名刺デザインはミスです
チラシデザインの作成を依頼します。
追加のデータです。
追加データです
以前出店の際に作っていただいたチラシデザインです。
イメージこのような形がいいです。
※マツエクは今回導入しません。
希望カラーをグレーにしましたが、
あまり暗い印象にはしたくありません。

あとスタイル写真複数枚載せてますが、
あまりごちゃごちゃにはしたくないので
人物写真は2〜3枚まででお願いします。

追加データで載せた以前のチラシのイメージで作って欲しいです。
mapも載せて欲しいです。
■ 選んだ理由

全体的にまとまりがあり、おしゃれ可愛さもあり
季節も考えてのカラーバリエーションなどのご提案もあって
とてもよかったです。

■ 提案者全員のお礼・コメント

この度は、弊社のコンペに参加・ご提案いただき誠に有り難うございました。

```html
<!DOCTYPE html>
<html lang="ja">
<head>
<meta charset="utf-8">
<title>K.A.Z by sorvique 仙台店 NEW OPEN</title>
<link rel="stylesheet" href="https://fonts.googleapis.com/css2?family=Bodoni+Moda:wght@500;600&family=Noto+Serif+JP:wght@500;700&family=Noto+Sans+JP:wght@400;500;700&display=swap">
<style>
  :root {
    --ink: #1c1c1c;
    --paper: #ffffff;
    --mist: #e9e8e6;
    --stone: #b9b6b2;
    --hair: #d58a5a;
    --blush: #d9a0a2;
    --present: #c98e96;
  }
  * { margin: 0; padding: 0; box-sizing: border-box; }
  html, body { width: 849px; height: 1200px; overflow: hidden; background: var(--paper); }
  .flyer {
    position: relative; width: 849px; height: 1200px; overflow: hidden;
    font-family: "Noto Sans JP", sans-serif; color: var(--ink);
  }
  .hero-photo {
    position: absolute; inset: 0;
    background:
      radial-gradient(ellipse 260px 340px at 260px 520px, #e7a27a 0%, #c97d55 45%, transparent 72%),
      radial-gradient(ellipse 300px 260px at 250px 920px, #7a6a5e 0%, #5c4f46 55%, transparent 80%),
      linear-gradient(180deg, #eef0ef 0%, #d9dcdc 40%, #bfc3c4 70%, #a9a9a6 100%);
  }
  .brand {
    position: absolute; top: 52px; left: 0; right: 0; text-align: center;
  }
  .brand-name {
    font-family: "Bodoni Moda", serif; font-weight: 500; font-size: 40px;
    letter-spacing: 4px; color: var(--ink);
  }
  .brand-kana {
    font-family: "Noto Serif JP", serif; font-size: 13px; letter-spacing: 3px; margin-top: 4px;
  }
  .tagline {
    position: absolute; top: 205px; left: 478px; width: 350px;
    font-family: "Noto Serif JP", serif; font-weight: 700; font-size: 36px;
    letter-spacing: 2px; transform: rotate(-8deg); text-align: center;
  }
  .tagline::after {
    content: ""; display: block; height: 2px; background: var(--ink); margin: 6px 20px 0;
  }
  .headline {
    position: absolute; top: 262px; left: 480px; width: 340px; text-align: center;
    font-family: "Bodoni Moda", serif; font-weight: 600; font-size: 118px; line-height: 104px;
    color: var(--ink);
  }
  .open-date {
    position: absolute; top: 500px; left: 545px;
    display: flex; align-items: center; gap: 8px;
    font-family: "Bodoni Moda", serif; font-weight: 600; font-size: 56px; color: var(--paper);
    text-shadow: 0 1px 6px rgba(0,0,0,.25);
  }
  .open-date .weekday {
    width: 44px; height: 44px; border-radius: 50%; background: var(--paper); color: var(--ink);
    font-family: "Noto Serif JP", serif; font-size: 22px; display: flex; align-items: center; justify-content: center;
    text-shadow: none;
  }
  .style-photo {
    position: absolute; top: 632px; left: 635px; width: 175px; height: 175px;
    border: 6px solid var(--paper);
    background: radial-gradient(circle at 50% 40%, #b58d6e 0%, #8a6a55 45%, #dcdcdc 80%);
  }
  .salon-photo {
    position: absolute; top: 745px; left: 505px; width: 190px; height: 160px;
    border: 6px solid var(--paper);
    background: linear-gradient(180deg, #f4f4f2 0%, #d8d6d2 55%, #3a3a3a 100%);
  }
  .info-band {
    position: absolute; left: 0; right: 0; bottom: 0; height: 155px; background: var(--paper);
  }
  .map {
    position: absolute; left: 22px; bottom: 16px; width: 225px; height: 123px;
    background: linear-gradient(135deg, #f2f2f2, #dedede); border: 1px solid var(--stone);
  }
  .shop {
    position: absolute; left: 262px; bottom: 20px;
  }
  .shop-name {
    font-family: "Noto Serif JP", serif; font-weight: 700; font-size: 22px; letter-spacing: 1px;
  }
  .shop-address { font-size: 11px; margin-top: 6px; }
  .shop-phone {
    display: flex; align-items: center; gap: 8px; margin-top: 6px;
    font-family: "Bodoni Moda", serif; font-weight: 600; font-size: 46px; letter-spacing: 1px;
  }
  .present {
    position: absolute; left: 620px; top: 975px; width: 250px; height: 250px; border-radius: 50%;
    background: var(--paper); border: 2px solid var(--mist);
    text-align: center; padding-top: 42px;
  }
  .present-note { font-size: 14px; letter-spacing: 1px; }
  .present-badge {
    display: inline-block; margin: 8px 0; padding: 6px 18px; background: var(--present); color: var(--paper);
    font-family: "Bodoni Moda", serif; font-weight: 600; font-size: 30px; letter-spacing: 2px;
  }
  .present-item { font-family: "Noto Serif JP", serif; font-size: 17px; line-height: 1.5; }
</style>
</head>
<body>
<div class="flyer">
  <div class="hero-photo" role="img" aria-label="オレンジブラウンのボブヘアの女性モデルと背景の街並み"></div>

  <header class="brand">
    <div class="brand-name">K.A.Z</div>
    <div class="brand-kana">美容室 カズ バイ ソルヴィーク</div>
  </header>

  <p class="tagline">仙台アーケード街に</p>
  <h1 class="headline">NEW<br>OPEN</h1>
  <p class="open-date">2022.6.1 <span class="weekday">水</span></p>

  <div class="style-photo" role="img" aria-label="ショートヘアのスタイル写真"></div>
  <div class="salon-photo" role="img" aria-label="白を基調としたサロン店内"></div>

  <section class="info-band">
    <div class="map" role="img" aria-label="仙台店周辺の地図"></div>
    <div class="shop">
      <p class="shop-name">K.A.Z by sorvique 仙台店</p>
      <p class="shop-address">仙台市青葉区中央1丁目2-3 ソルビル2F</p>
      <p class="shop-phone">
        <svg width="34" height="34" viewBox="0 0 24 24" aria-hidden="true"><path fill="#1c1c1c" d="M6.6 10.8a15.1 15.1 0 0 0 6.6 6.6l2.2-2.2a1 1 0 0 1 1-.25 11.4 11.4 0 0 0 3.6.57 1 1 0 0 1 1 1V20a1 1 0 0 1-1 1A17 17 0 0 1 3 4a1 1 0 0 1 1-1h3.5a1 1 0 0 1 1 1c0 1.25.2 2.45.57 3.6a1 1 0 0 1-.25 1z"/></svg>
        022-614-5027
      </p>
    </div>
  </section>

  <aside class="present">
    <p class="present-note">このチラシご持参で</p>
    <p class="present-badge">PRESENT</p>
    <p class="present-item">トリートメント<br>プレゼント</p>
  </aside>
</div>
</body>
</html>
```